Consumer Protection Law Firm Needs a New Website

We need a new website for our law firm. We practice consumer protection law, with an emphasis on class actions. In particular, we serve consumers who are harassed by telemarketers, debt collectors, abusive companies, and financial criminals. In short, we sue big companies that do bad things to lots of people.

The lawyer is Tomas Fenwald. Current website is available through www.FenwaldLegal.example. Some logo files are attached.

Prefer designs that use the colors black, red, and white, per the logo. Also prefer clean, lightweight HTML5/CSS3 design rather than Wordpress. Finally, single-page type design preferred over multi-page, but flexible.

I have some limited familiarity with HTML and CSS, particularly Bootstrap, so a Bootstrap type design that I can modify myself would be ideal.

Target Market(s)

Consumers with cellular telephones.

Industry/Entity Type

Law Firm

Coding

Coded - Design and coding required

Number of Pages Required

1 page

Requirements
Must have
• - Mobile friendly, preferably without requiring separate design. In other words, a framework like Bootstrap is preferred.
• - Contact Form
• - A section for recent results
• - A section for a picture and bio of Tomas Fenwald, Esq.
Nice to have
• - Animated elements that count-up and populate with numbers for things like:
• * X dollars recovered for consumers.
• * Y clients represented
• * Over Z lawsuits filed for consumers

```html
<!DOCTYPE html>
<html lang="en">
<head>
<meta charset="utf-8">
<title>Tomas Fenwald — Consumer Advocate</title>
<link rel="stylesheet" href="https://fonts.googleapis.com/css2?family=Open+Sans:wght@300;400&family=Roboto:wght@300;400;500&display=swap">
<style>
  :root {
    --dark: #3a3a3a;
    --light-bg: #eeeeee;
    --white: #ffffff;
    --text: #555555;
    --muted: #777777;
    --icon: #666666;
    --border: #dddddd;
    --orange: #ff9900;
  }
  * { box-sizing: border-box; margin: 0; padding: 0; }
  html, body { width: 1200px; height: 1102px; overflow: hidden; }
  body {
    background: var(--light-bg);
    font-family: "Open Sans", sans-serif;
    color: var(--text);
    position: relative;
  }
  .hero-band {
    position: absolute; left: 0; top: 0; width: 1200px; height: 499px;
    background: var(--dark);
  }
  .site-nav {
    position: absolute; top: 0; left: 162px; width: 873px; height: 58px;
    font-family: "Roboto", sans-serif; font-weight: 300; font-size: 13px; color: var(--white);
  }
  .site-nav a { color: var(--white); text-decoration: none; position: absolute; top: 20px; }
  .site-nav .active::after {
    content: ""; position: absolute; left: -12px; right: -12px; top: 37px;
    height: 1px; background: var(--white);
  }
  .brand {
    position: absolute; left: 0; right: 0; top: 17px; text-align: center;
    font-family: "Roboto", sans-serif; font-weight: 400; font-size: 14px; color: var(--white);
  }
  .brand-mark {
    display: inline-block; width: 10px; height: 10px; background: var(--white);
    margin-right: 7px; vertical-align: 0;
  }
  .hero {
    position: absolute; top: 158px; left: 162px; width: 873px; text-align: center; color: var(--white);
  }
  .hero h1 {
    font-family: "Roboto", sans-serif; font-weight: 300; font-size: 26px; line-height: 38px;
  }
  .hero-rule { width: 160px; height: 1px; background: var(--white); margin: 28px auto 33px; }
  .hero p { font-size: 12.5px; line-height: 16px; letter-spacing: -0.2px; }
  .btn-outline {
    display: inline-block; margin-top: 28px; width: 152px; height: 41px; line-height: 39px;
    border: 1px solid var(--white); color: var(--white); text-decoration: none;
    font-family: "Roboto", sans-serif; font-weight: 300; font-size: 13px;
  }
  .cta-card {
    position: absolute; left: 162px; top: 467px; width: 873px; height: 157px;
    background: var(--white); border: 1px solid var(--border);
  }
  .cta-card h2 {
    position: absolute; left: 32px; top: 31px;
    font-family: "Roboto", sans-serif; font-weight: 300; font-size: 19px; color: var(--text);
  }
  .cta-card p {
    position: absolute; left: 32px; top: 70px; width: 580px;
    font-family: "Roboto", sans-serif; font-weight: 300; font-size: 14.5px; line-height: 19px; color: var(--text);
  }
  .btn-consult {
    position: absolute; left: 651px; top: 33px; width: 189px; height: 65px;
    background: var(--orange); color: var(--white); text-decoration: none; text-align: center;
    font-family: "Roboto", sans-serif; font-size: 12.5px; line-height: 18px; padding-top: 14px;
  }
  .btn-consult span { font-weight: 300; display: block; }
  .btn-consult strong { font-weight: 500; }
  .services {
    position: absolute; left: 162px; top: 657px; width: 873px; height: 460px;
    background: var(--white); border: 1px solid var(--border);
    display: grid; grid-template-columns: repeat(3, 1fr); grid-auto-rows: 184px;
    padding: 31px 32px 0; row-gap: 0;
  }
  .service { text-align: center; }
  .service-icon {
    width: 51px; height: 51px; border: 1px solid var(--icon); border-radius: 50%;
    margin: 0 auto; display: flex; align-items: center; justify-content: center;
  }
  .service-icon svg { width: 24px; height: 24px; fill: var(--icon); }
  .service h3 {
    font-family: "Roboto", sans-serif; font-weight: 300; font-size: 15px; color: var(--text);
    margin-top: 12px;
  }
  .service p {
    font-weight: 300; font-size: 12px; line-height: 16px; color: var(--muted);
    margin: 13px auto 0; width: 250px;
  }
</style>
</head>
<body>
  <div class="hero-band"></div>

  <nav class="site-nav">
    <a href="#" class="active" style="left:12px">Home</a>
    <a href="#" style="left:70px">Firm</a>
    <a href="#" style="left:120px">Practice Areas</a>
    <a href="#" style="left:225px">News</a>
    <div class="brand"><span class="brand-mark"></span>Fenwald Legal</div>
    <a href="#" style="left:768px">Contact</a>
    <a href="#" style="left:836px">FAQ</a>
  </nav>

  <header class="hero">
    <h1>Consumer Advocate</h1>
    <div class="hero-rule"></div>
    <p>Tomas Fenwald is passionate about representing victims of abusive debt collectors, illegal telemarketing, and text message spam. Contact us for a free consultation if you have a matter you would like to discuss!</p>
    <a href="#" class="btn-outline">Contact Us Now!</a>
  </header>

  <section class="cta-card">
    <h2>Are you being harassed by debt collectors?</h2>
    <p>Unlawful telephone harassment is a serious violation of your rights. Don't stand for it. Contact attorney Tomas Fenwald today.</p>
    <a href="#" class="btn-consult"><span>Click Here now for your</span><strong>Free Consultation</strong></a>
  </section>

  <section class="services">
    <article class="service">
      <div class="service-icon"><svg viewBox="0 0 24 24"><path d="M12 2 4 5v6c0 5 3.4 9.6 8 11 4.6-1.4 8-6 8-11V5zm0 2.2V12H6V6.4zM12 12h6c-.4 4-2.9 7.5-6 8.7z"/></svg></div>
      <h3>Consumer Protection</h3>
      <p>Tomas Fenwald is versed in the law of unlawful debt collection practices, and holds offenders accountable in court.</p>
    </article>
    <article class="service">
      <div class="service-icon"><svg viewBox="0 0 24 24"><path d="M3 5h7l2 2h9v12H3zm9 4a2 2 0 1 0 0 4 2 2 0 0 0 0-4zm-4 8h8c0-2-1.8-3-4-3s-4 1-4 3z" fill-rule="evenodd"/></svg></div>
      <h3>Debtor Rights</h3>
      <p>Tomas Fenwald analyzes debt collection lawsuits, breaks them down, and enforces the rights of distressed consumers.</p>
    </article>
    <article class="service">
      <div class="service-icon"><svg viewBox="0 0 24 24"><path d="M6.6 10.8a15 15 0 0 0 6.6 6.6l2.2-2.2c.3-.3.7-.4 1-.2 1.1.4 2.3.6 3.6.6.6 0 1 .4 1 1V20c0 .6-.4 1-1 1A17 17 0 0 1 3 4c0-.6.4-1 1-1h3.5c.6 0 1 .4 1 1 0 1.3.2 2.5.6 3.6.1.3 0 .7-.2 1z"/><path d="M16 5a2 2 0 0 1 4 0v1h1v5h-6V6h1zm1 1h2V5a1 1 0 0 0-2 0z"/></svg></div>
      <h3>Telephone Harassment</h3>
      <p>If you have been the subject of constant or abusive telephone calls, contact us for a free consultation.</p>
    </article>
    <article class="service">
      <div class="service-icon"><svg viewBox="0 0 24 24" fill="none" stroke="#666" stroke-width="2"><circle cx="12" cy="12" r="7"/><path d="M12 2v3M12 19v3M2 12h3M19 12h3M4 4l16 16"/></svg></div>
      <h3>Privacy</h3>
      <p>New privacy concerns emerge on an almost-daily basis. If you believe your privacy rights have been violated, contact us for a free consultation.</p>
    </article>
    <article class="service">
      <div class="service-icon"><svg viewBox="0 0 24 24"><path d="M6.6 10.8a15 15 0 0 0 6.6 6.6l2.2-2.2c.3-.3.7-.4 1-.2 1.1.4 2.3.6 3.6.6.6 0 1 .4 1 1V20c0 .6-.4 1-1 1A17 17 0 0 1 3 4c0-.6.4-1 1-1h3.5c.6 0 1 .4 1 1 0 1.3.2 2.5.6 3.6.1.3 0 .7-.2 1z"/><path d="M13 3h8v6h-5l-3 2z"/></svg></div>
      <h3>Text Message Spam</h3>
      <p>Text message spam is the newest form of abusive telemarketing. When advertisers cross the line, Tomas Fenwald sues them and holds them accountable.</p>
    </article>
    <article class="service">
      <div class="service-icon"><svg viewBox="0 0 24 24"><path d="M12 1l2.8 2.4 3.6-.3.8 3.6 3.1 1.9-1.5 3.4 1.5 3.4-3.1 1.9-.8 3.6-3.6-.3L12 23l-2.8-2.4-3.6.3-.8-3.6-3.1-1.9L3.2 12 1.7 8.6l3.1-1.9.8-3.6 3.6.3zM11 6v8h2V6zm0 10v2h2v-2z" fill-rule="evenodd"/></svg></div>
      <h3>Criminal Law</h3>
      <p>In America, those accused of crimes have basic rights. Enforcing those rights requires the advice &amp; representation of a competent attorney.</p>
    </article>
  </section>
</body>
</html>
```